Design Cloud for Core Values & Attributes

See Image Example Below "Word Cloud" this is what we would like this to look like.
The second image is all of the Core Value and Attributes I will list below.
CORE VALUES need to be the bigger words (based off the image I sent) Capitalized, BOLD, Navy
Independence, Capitalism, Trust, Fun, Safety, Growth
ATTRIBUTES need to be the smaller words, lower case, non-bold, lighter blue mixed in (based off the image I sent):
Humility, Consistency, Open Mindedness, Curiosity, Selflessness, Caring, Conscientiousness, Honorable, Cunning, Competitive, Compartmentalization, Innovative, Perseverance, Authenticity, Decisiveness, Self-efficacy, Accountability, Generosity, Humor, Optimism, Resilience, Inclusive, Insouciance to what others think, Courage, Decisive, Curious, Integrity

```html
<!DOCTYPE html>
<html lang="en">
<head>
<meta charset="UTF-8">
<title>Core Values &amp; Attributes Word Cloud</title>
<link href="https://fonts.googleapis.com/css2?family=Barlow+Condensed:wght@600;700&display=swap" rel="stylesheet">
<style>
  :root {
    --bg: #f4f4f4;
    --navy: #1f4080;
    --sky: #0f9bd8;
  }
  * { margin: 0; padding: 0; box-sizing: border-box; }
  html, body {
    width: 912px;
    height: 1200px;
    overflow: hidden;
    background: var(--bg);
  }
  .canvas {
    position: relative;
    width: 912px;
    height: 1200px;
    background: var(--bg);
    overflow: hidden;
  }
  .word-cloud {
    position: absolute;
    left: 0;
    top: 358px;
    width: 1680px;
    height: 900px;
    transform: scale(0.542857);
    transform-origin: 0 0;
    font-family: "Barlow Condensed", "Arial Narrow", sans-serif;
  }
  .word {
    position: absolute;
    line-height: 1;
    white-space: nowrap;
  }
  .value {
    color: var(--navy);
    font-weight: 700;
    text-transform: uppercase;
  }
  .attribute {
    color: var(--sky);
    font-weight: 600;
  }
  .vertical-down {
    writing-mode: vertical-rl;
  }
  .vertical-up {
    writing-mode: vertical-rl;
    transform: rotate(180deg);
  }
</style>
</head>
<body>
<main class="canvas">
  <section class="word-cloud" aria-label="Core values and attributes">
    <!-- Core values -->
    <span class="word value vertical-up" style="left:666px; top:95px; font-size:136px;">Trust</span>
    <span class="word value" style="left:803px; top:320px; font-size:90px;">Capitalism</span>
    <span class="word value" style="left:492px; top:409px; font-size:130px;">Independence</span>
    <span class="word value" style="left:478px; top:536px; font-size:110px;">Safety</span>
    <span class="word value vertical-down" style="left:811px; top:545px; font-size:86px;">Growth</span>
    <span class="word value" style="left:916px; top:531px; font-size:104px;">Fun</span>

    <!-- Attributes -->
    <span class="word attribute" style="left:826px; top:121px; font-size:34px;">Insouciance to what others think</span>
    <span class="word attribute" style="left:826px; top:171px; font-size:34px;">Accountability</span>
    <span class="word attribute" style="left:1032px; top:166px; font-size:60px;">Courage</span>
    <span class="word attribute" style="left:825px; top:225px; font-size:34px;">Perseverance</span>
    <span class="word attribute" style="left:1031px; top:233px; font-size:34px;">Decisive</span>
    <span class="word attribute" style="left:825px; top:273px; font-size:44px;">Conscientiousness</span>
    <span class="word attribute vertical-up" style="left:638px; top:113px; font-size:36px;">Compartmentalization</span>
    <span class="word attribute" style="left:478px; top:283px; font-size:34px;">Resilience</span>
    <span class="word attribute" style="left:415px; top:316px; font-size:48px;">Innovative</span>
    <span class="word attribute" style="left:526px; top:375px; font-size:34px;">Caring</span>
    <span class="word attribute" style="left:350px; top:490px; font-size:34px;">Inclusive</span>
    <span class="word attribute" style="left:1248px; top:487px; font-size:34px;">Generosity</span>
    <span class="word attribute" style="left:345px; top:535px; font-size:34px;">Optimism</span>
    <span class="word attribute" style="left:299px; top:573px; font-size:34px;">Decisiveness</span>
    <span class="word attribute" style="left:1091px; top:539px; font-size:34px;">Humility</span>
    <span class="word attribute" style="left:1221px; top:539px; font-size:34px;">Self-efficacy</span>
    <span class="word attribute" style="left:1085px; top:581px; font-size:44px;">Open Mindedness</span>
    <span class="word attribute" style="left:900px; top:638px; font-size:34px;">Consistency</span>
    <span class="word attribute" style="left:1086px; top:631px; font-size:54px;">Humor</span>
    <span class="word attribute" style="left:900px; top:676px; font-size:34px;">Honorable</span>
    <span class="word attribute" style="left:399px; top:644px; font-size:54px;">Authenticity</span>
    <span class="word attribute" style="left:654px; top:645px; font-size:34px;">Curiosity</span>
    <span class="word attribute" style="left:666px; top:683px; font-size:34px;">Cunning</span>
    <span class="word attribute vertical-down" style="left:785px; top:645px; font-size:31px;">Competitive</span>
    <span class="word attribute" style="left:396px; top:704px; font-size:56px;">Integrity</span>
    <span class="word attribute" style="left:606px; top:725px; font-size:34px;">Selflessness</span>
    <span class="word attribute" style="left:899px; top:713px; font-size:60px;">Curious</span>
  </section>
</main>
</body>
</html>
```